Tamarind Crest Management - Business Cards

I need business cards. My current logo was designed by a designer at this site and I very much like and am happy with the results. I would like a business card that is trendy, unique, current yet professional. I deal with high net worth clients daily

Target Market(s)

Out of state investors looking to get into the rental market in Ohio

Industry/Entity Type

Property Management, Consulting

Contact Information for Business Card

Name, Title (Chief Financial Officer) office phone number (347) 681-9072 website address tamcrestmgmt.example

Font styles to use
Sans Serif

Colors
0054AA
0677BA
7BADD7
CADEEF
E8F1F8
0094D4
00A9DD
6FCCEA
C7EBF8
E9F6FB
00AB8E
00BBA5
67D7C9
C6EFE9
E9F9F6

```html
<!DOCTYPE html>
<html lang="en">
<head>
<meta charset="utf-8">
<title>Tamarind Crest Management – Business Cards</title>
<link href="https://fonts.googleapis.com/css2?family=Lato:wght@400;700;900&display=swap" rel="stylesheet">
<style>
  :root{
    --bg:#e9edf1;
    --card:#ffffff;
    --navy:#1f3560;
    --blue:#2a5aa5;
    --blue-text:#0054aa;
    --teal:#00ab8e;
    --grey:#4a4a4a;
    --white:#ffffff;
  }
  *{box-sizing:border-box;margin:0;padding:0}
  html,body{width:1200px;height:875px;overflow:hidden}
  body{background:var(--bg);font-family:"Lato",sans-serif;position:relative}
  .card{
    position:absolute;left:300px;width:600px;height:343px;
    background:var(--card);border-radius:22px;overflow:hidden;
    box-shadow:0 10px 28px rgba(0,0,0,.18);
  }
  .card--front{top:72px}
  .card--back{top:460px}

  .wordmark{display:flex;align-items:center;gap:14px}
  .wordmark__mark{width:22px;height:22px;background:var(--navy);flex:none}
  .wordmark__name{font-weight:900;color:var(--navy);text-transform:uppercase;line-height:1.05;letter-spacing:.5px}
  .card--front .wordmark{position:absolute;left:50%;top:50%;transform:translate(-50%,-50%)}
  .card--front .wordmark__name{font-size:30px}
  .card--back .wordmark{position:absolute;left:40px;top:100px;width:230px}
  .card--back .wordmark__name{font-size:22px}

  .back-wave{position:absolute;inset:0;width:100%;height:100%}
  .accent-bar{position:absolute;right:0;top:22px;width:10px;height:42px;background:var(--blue)}

  .person{position:absolute;right:34px;top:26px;text-align:right}
  .person__name{font-weight:700;font-size:24px;color:var(--blue-text);letter-spacing:.3px}
  .person__title{font-size:14px;color:var(--grey);margin-top:2px}

  .contact{position:absolute;right:28px;top:130px;list-style:none;text-align:right;color:var(--white);font-size:14px;line-height:22px}
  .contact li{display:flex;justify-content:flex-end;align-items:center;gap:10px}
  .contact svg{width:14px;height:14px;flex:none}
  .contact .spacer{width:14px;flex:none}
</style>
</head>
<body>

<section class="card card--front">
  <div class="wordmark">
    <span class="wordmark__mark"></span>
    <span class="wordmark__name">Tamarind Crest<br>Management</span>
  </div>
</section>

<section class="card card--back">
  <svg class="back-wave" viewBox="0 0 600 343" preserveAspectRatio="none" aria-hidden="true">
    <path d="M0,343 V312 C150,308 250,270 305,175 C355,92 430,82 600,78 V343 Z" fill="var(--blue)"/>
    <path d="M0,300 C120,296 205,262 250,170 C215,250 130,292 0,290 Z" fill="var(--teal)"/>
    <path d="M150,330 C250,300 300,230 340,160 C380,95 420,80 470,70 C420,92 390,120 355,175 C315,245 260,305 150,330 Z" fill="var(--white)"/>
  </svg>
  <span class="accent-bar"></span>

  <div class="wordmark">
    <span class="wordmark__mark"></span>
    <span class="wordmark__name">Tamarind Crest<br>Management</span>
  </div>

  <div class="person">
    <p class="person__name">MARCUS WHITFIELD</p>
    <p class="person__title">Chief Financial Officer</p>
  </div>

  <ul class="contact">
    <li>(347) 681-9072
      <svg viewBox="0 0 24 24"><path fill="var(--teal)" d="M6.6 10.8a15 15 0 0 0 6.6 6.6l2.2-2.2c.3-.3.7-.4 1-.2 1.1.4 2.3.6 3.6.6.6 0 1 .4 1 1V20c0 .6-.4 1-1 1A17 17 0 0 1 3 4c0-.6.4-1 1-1h3.5c.6 0 1 .4 1 1 0 1.3.2 2.5.6 3.6.1.3 0 .7-.2 1z"/></svg></li>
    <li>info@tamcrestmgmt.example
      <svg viewBox="0 0 24 24"><rect x="2" y="5" width="20" height="14" rx="1" fill="var(--teal)"/><path d="M2 6l10 7 10-7" fill="none" stroke="var(--blue)" stroke-width="1.6"/></svg></li>
    <li>www.tamcrestmgmt.example
      <svg viewBox="0 0 24 24"><circle cx="12" cy="12" r="10" fill="var(--teal)"/><path d="M2 12h20M12 2c3 3 3 17 0 20M12 2c-3 3-3 17 0 20" fill="none" stroke="var(--blue)" stroke-width="1.4"/></svg></li>
    <li>421, Address line goes here<span class="spacer"></span></li>
    <li>45452, Country name<span class="spacer"></span></li>
  </ul>
</section>

</body>
</html>
```